Commercial Construction Company

We need a business card design based on our current logo. We are a commercial general contractor based in Southern California that specializes in bank remodels. We would like to see designs that incorporate dark blue. The final design should portray an image of professionalism and quality.

If possible, I would like to add metallic foil to the design. Thank you

```html
<!DOCTYPE html>
<html lang="en">
<head>
<meta charset="utf-8">
<title>Halden Commercial – Business Card</title>
<link rel="stylesheet" href="https://fonts.googleapis.com/css2?family=Open+Sans:wght@400;700;800&display=swap">
<style>
  :root {
    --navy: #134a82;
    --navy-light: #3f7fc4;
    --silver: #c8cbd0;
    --grey: #a9abae;
    --ink: #111111;
    --text: #4a4a4a;
    --paper: #ffffff;
    --backdrop: #3b3734;
  }
  * { margin: 0; padding: 0; box-sizing: border-box; }
  html, body { width: 1200px; height: 900px; overflow: hidden; }
  body {
    background: var(--backdrop);
    font-family: "Open Sans", Arial, sans-serif;
    position: relative;
  }
  .card {
    position: absolute;
    left: 250px;
    width: 700px;
    height: 400px;
    overflow: hidden;
    box-shadow: 0 10px 30px rgba(0,0,0,.45);
  }
  .card-front { top: 40px; background: var(--navy); }
  .card-back { top: 460px; background: var(--paper); }

  .brand {
    position: absolute;
    display: flex;
    align-items: center;
    gap: 12px;
    font-weight: 800;
    letter-spacing: .5px;
    white-space: nowrap;
  }
  .brand-dot { border-radius: 50%; flex: none; }
  .card-front .brand {
    left: 0; right: 0; top: 170px;
    justify-content: center;
    font-size: 38px;
    color: var(--silver);
  }
  .card-front .brand-dot { width: 44px; height: 44px; background: var(--silver); }
  .card-back .brand {
    left: 45px; top: 158px;
    font-size: 24px;
    color: var(--ink);
  }
  .card-back .brand-dot { width: 30px; height: 30px; background: var(--grey); }

  .divider {
    position: absolute;
    left: 370px; top: 45px;
    width: 2px; height: 185px;
    background: var(--navy);
  }
  .contact { position: absolute; left: 390px; top: 40px; color: var(--text); white-space: nowrap; }
  .contact-name {
    font-size: 23px; font-weight: 800; color: var(--navy);
    letter-spacing: .5px; line-height: 1.2;
  }
  .contact-title { font-size: 16px; line-height: 1.35; margin-bottom: 8px; }
  .contact-address { font-size: 16px; line-height: 1.3; margin-bottom: 6px; }
  .contact-line {
    display: flex; align-items: center; gap: 8px;
    font-size: 16px; line-height: 1.3;
  }
  .contact-line svg { width: 13px; height: 13px; flex: none; fill: var(--navy); }

  .wave { position: absolute; left: 0; top: 0; width: 700px; height: 400px; }
  .website {
    position: absolute; left: 180px; bottom: 20px;
    font-size: 16px; color: var(--paper);
  }
</style>
</head>
<body>

<section class="card card-front">
  <div class="brand">
    <span class="brand-dot"></span>
    <span class="brand-name">Halden Commercial</span>
  </div>
</section>

<section class="card card-back">
  <svg class="wave" viewBox="0 0 700 400" aria-hidden="true">
    <path d="M340 292 C480 280 630 240 700 150 L700 185 C630 255 490 288 340 292 Z" fill="#a9abae"/>
    <path d="M100 400 C150 325 255 298 420 290 C560 280 650 245 700 195 L700 205 C650 255 560 290 420 300 C270 310 170 335 120 400 Z" fill="#3f7fc4"/>
    <path d="M120 400 C170 335 270 310 420 300 C560 290 650 255 700 205 L700 400 Z" fill="#134a82"/>
  </svg>

  <div class="brand">
    <span class="brand-dot"></span>
    <span class="brand-name">Halden Commercial</span>
  </div>

  <div class="divider"></div>

  <div class="contact">
    <div class="contact-name">DANIEL REYES</div>
    <div class="contact-title">President</div>
    <div class="contact-address">1480 Harbor View Drive<br>Newport CA 92660</div>
    <div class="contact-line">
      <svg viewBox="0 0 24 24"><path d="M6.6 10.8a15 15 0 0 0 6.6 6.6l2.2-2.2c.3-.3.7-.4 1-.2 1.1.4 2.3.6 3.6.6.6 0 1 .4 1 1V20c0 .6-.4 1-1 1A17 17 0 0 1 3 4c0-.6.4-1 1-1h3.5c.6 0 1 .4 1 1 0 1.3.2 2.5.6 3.6.1.3 0 .7-.2 1z"/></svg>
      <span>555-210-4837</span>
    </div>
    <div class="contact-line">
      <svg viewBox="0 0 24 24"><path d="M7 1h10a2 2 0 0 1 2 2v18a2 2 0 0 1-2 2H7a2 2 0 0 1-2-2V3a2 2 0 0 1 2-2zm0 3v14h10V4zm5 15.5a1 1 0 1 0 0 2 1 1 0 0 0 0-2z"/></svg>
      <span>555-210-4837</span>
    </div>
    <div class="contact-line">
      <svg viewBox="0 0 24 24"><path d="M2 5h20v14H2zm2 2v.5l8 5 8-5V7z"/></svg>
      <span>daniel@haldenbuild.com</span>
    </div>
  </div>

  <div class="website">www.haldenbuild.com</div>
</section>

</body>
</html>
```